Brindle's Online: Logo Banner Graphic-

We are building our website and need to take our current logo ( that you designed) and create a banner with our tagline. The key focus is that we need to play with color on the logo that fits to the current background- The goal is to make it "pop" without making it look cheap. This is a high end lifestyle brand.

We are open to color( and will consider changing the background for the right look and open to you creating a new background to work with the design) but keeping in mind it needs to have color that represent luxury, money, leisure.

The sizing/pixels should be
2510 x 1671 px
8.37 x 5.57p

Currently you can look at the prototype website at

www.brindlesonline-example.com

Please let me know if you have any questions.
Updates

Target Market(s)

30 plus

Industry/Entity Type

Building

Font styles to use
Sans Serif

Requirements
Must have
• Logo and tagline in header
Nice to have
• open
Should not have
• color to make it pop on website. It needs to be professional and polished not cheap looking.

```html
<!DOCTYPE html>
<html lang="en">
<head>
<meta charset="utf-8">
<title>Brindle's Online – Banner</title>
<link rel="stylesheet" href="https://fonts.googleapis.com/css2?family=Cabin+Condensed:wght@400&display=swap">
<style>
  :root {
    --navy-light: #223766;
    --navy-mid: #1a2b57;
    --navy-deep: #0f1a3b;
    --ivory: #ffffff;
  }
  html, body {
    margin: 0;
    padding: 0;
    width: 1200px;
    height: 799px;
    overflow: hidden;
    background: var(--navy-deep);
  }
  .banner {
    position: relative;
    width: 1200px;
    height: 799px;
    overflow: hidden;
    background: radial-gradient(ellipse 85% 95% at 30% 20%, var(--navy-light) 0%, var(--navy-mid) 45%, var(--navy-deep) 100%);
    font-family: "Cabin Condensed", sans-serif;
    color: var(--ivory);
  }
  .frame {
    position: absolute;
    inset: 0;
    width: 1200px;
    height: 799px;
  }
  .brand-mark {
    position: absolute;
    left: 0;
    top: 90px;
    width: 1200px;
    height: 362px;
    display: flex;
    flex-direction: column;
    align-items: center;
    justify-content: flex-start;
    gap: 26px;
  }
  .brand-disc {
    width: 230px;
    height: 230px;
    border-radius: 50%;
    background: var(--ivory);
    flex: none;
  }
  .brand-name {
    margin: 0;
    font-size: 92px;
    font-weight: 400;
    letter-spacing: 6px;
    line-height: 1;
    text-transform: uppercase;
  }
  .tagline {
    position: absolute;
    left: 0;
    top: 487px;
    width: 1200px;
    margin: 0;
    text-align: center;
    font-size: 62px;
    font-weight: 400;
    line-height: 69px;
    letter-spacing: 1px;
    text-transform: uppercase;
  }
</style>
</head>
<body>
  <main class="banner">
    <svg class="frame" viewBox="0 0 1200 799" aria-hidden="true">
      <rect x="17" y="18" width="1166" height="764" fill="none" stroke="var(--ivory)" stroke-width="2"/>
      <rect x="32" y="35" width="1136" height="729" fill="none" stroke="var(--ivory)" stroke-width="1.5"/>
    </svg>

    <div class="brand-mark">
      <span class="brand-disc" aria-hidden="true"></span>
      <h1 class="brand-name">Brindle's</h1>
    </div>

    <p class="tagline">
      Delivering simplified,<br>
      reliable products<br>
      to fit your lifestyle
    </p>
  </main>
</body>
</html>
```